Wealth Management Business Card

We are a professional services consulting firm that specializes in high net worth individuals over $25,000,000, executives C-suite and above, closely held businesses owners, family offices and highly compensated employees.

Our focus is on risk mitigation and tax efficient strategies. Our clients take their risk on themselves and have a proven track record generating wealth. Our directive is to preserve and protect the wealth they’ve already created.

Our company Harbridge Advisory is geared around five directives of asset protection:
1) Legal Structuring
2) Leverage & Financing
3) Risk Management - Asset Protection & Insurance, Trustee Work
4) Asset Management & Investing - Under www.qelvantcapital.com
5) Tax Efficient Strategies

Our Company Mark is a Pentagon with a key in the middle. A pentagon is the most efficient defensive structure. Each point of a pentagon is equal distance front every point . Each side provides support to another and works together, which is the key to our clients success.

Our key colors are blue, black and silver.

We ‘re located in the Pacific Northwest with bi coastal and international clients. We have fewer, higher net worth clients and provide exceptional customer service. We do not do social media.

website is www.harbridgepath.com

Target Market(s)

High End Clients

Contact Information for Business Card

extra thick

Font styles to use
Serif

Requirements
Must have
• Metalic foil for lettering.
Black Background on one side
White Background on the other
Horizontal Format Only
No Rounded corners
Not Marketing sales information on the card.
Nice to have
• imprinted texture on the card
Should not have
• lots of color

```html
<!DOCTYPE html>
<html lang="en">
<head>
<meta charset="utf-8">
<title>Harbridge Advisory — Business Card</title>
<link href="https://fonts.googleapis.com/css2?family=Cinzel:wght@500;600&family=Poppins:wght@300;400&display=swap" rel="stylesheet">
<style>
  :root {
    --page: #e4e4e4;
    --paper: #ffffff;
    --navy: #0b2a6b;
    --navy-deep: #06205c;
    --sky: #1a9be0;
    --ink: #555a60;
    --black-card-a: #121212;
    --black-card-b: #3c3c3c;
    --silver: #c9ccd1;
  }
  * { margin: 0; padding: 0; box-sizing: border-box; }
  html, body { width: 1200px; height: 1200px; overflow: hidden; background: var(--page); }
  .canvas { position: relative; width: 1200px; height: 1200px; }

  .card { position: absolute; left: 262px; width: 686px; height: 392px; }
  .card--front { top: 165px; background: var(--paper); }
  .card--back {
    top: 653px;
    background: linear-gradient(120deg, var(--black-card-a) 0%, #1e1e1e 50%, var(--black-card-b) 100%);
  }

  .front__band {
    position: absolute; left: 0; right: 0; bottom: 0; height: 14px;
    background: linear-gradient(90deg, var(--navy-deep), #123a80 60%, var(--navy-deep));
  }

  .brand {
    position: absolute; display: flex; flex-direction: column; align-items: center;
    font-family: "Cinzel", serif; font-weight: 600; text-transform: uppercase; line-height: 1.1;
  }
  .brand__mark { width: 54px; height: 54px; margin-bottom: 18px; }
  .brand__name { font-size: 28px; letter-spacing: 1px; text-align: center; }

  .brand--front { left: 40px; width: 310px; top: 118px; color: var(--navy); }
  .brand--front .brand__mark { background: var(--navy); }

  .brand--back { left: 0; right: 0; top: 110px; color: var(--silver); }
  .brand--back .brand__mark { background: var(--silver); width: 64px; height: 64px; margin-bottom: 24px; }
  .brand--back .brand__name { font-size: 36px; letter-spacing: 2px; }

  .divider { position: absolute; left: 333px; top: 114px; width: 1.5px; height: 164px; background: var(--navy); }

  .contact { position: absolute; left: 366px; top: 120px; font-family: "Poppins", sans-serif; font-weight: 300; color: var(--ink); }
  .contact__name {
    font-family: "Cinzel", serif; font-weight: 500; font-size: 23px; color: var(--navy);
    line-height: 1; letter-spacing: 0.5px;
  }
  .contact__title { font-size: 14.5px; color: var(--sky); margin-top: 4px; letter-spacing: 0.3px; }
  .contact__address { font-size: 15.5px; line-height: 19px; margin-top: 14px; }
  .contact__lines { list-style: none; margin-top: 14px; font-size: 16px; line-height: 20px; }
  .contact__lines li { display: flex; align-items: center; gap: 8px; }
  .contact__lines svg { width: 13px; height: 13px; flex: none; fill: var(--sky); }
</style>
</head>
<body>
<div class="canvas">

  <section class="card card--front" aria-label="Card front">
    <div class="brand brand--front">
      <span class="brand__mark" aria-hidden="true"></span>
      <span class="brand__name">Harbridge<br>Advisory</span>
    </div>

    <span class="divider" aria-hidden="true"></span>

    <div class="contact">
      <p class="contact__name">Marcus Ellery</p>
      <p class="contact__title">Financial Strategist &amp; Founder</p>
      <p class="contact__address">1427 Alder Ridge Rd, Suite 310<br>Cedar Falls, OR 97218</p>
      <ul class="contact__lines">
        <li>
          <svg viewBox="0 0 16 16" aria-hidden="true"><path d="M3.6 1.2l2.3 2.9-1.3 1.8c.9 2 2.5 3.6 4.5 4.5l1.8-1.3 2.9 2.3-1.4 2.4C7.6 13.6 2.4 8.4 1.2 3.6z"/></svg>
          (503) 555-0147
        </li>
        <li>
          <svg viewBox="0 0 16 16" aria-hidden="true"><path d="M1 3.5h14v9H1z M1.6 4l6.4 4.8L14.4 4"/><path d="M1.8 4.2L8 8.8l6.2-4.6" fill="none" stroke="#fff" stroke-width="1.1"/></svg>
          info@harbridgepath.com
        </li>
        <li>
          <svg viewBox="0 0 16 16" aria-hidden="true"><circle cx="8" cy="8" r="7"/><path d="M5 4.5c1.5.5 2 1.6 1.2 2.6-.8.9.2 2 1.3 2.2.8.2.9 1.3.4 2.2M10.5 3.6c-.6 1-.1 2 1.2 2.3" fill="none" stroke="#fff" stroke-width="1.1"/></svg>
          harbridgepath.com
        </li>
      </ul>
    </div>

    <span class="front__band" aria-hidden="true"></span>
  </section>

  <section class="card card--back" aria-label="Card back">
    <div class="brand brand--back">
      <span class="brand__mark" aria-hidden="true"></span>
      <span class="brand__name">Harbridge Advisory</span>
    </div>
  </section>

</div>
</body>
</html>
```